Real Estate Company Needs Business Card Designed

We need a business card design for a new real estate company based in Campbell, CA (Silicon Valley). We plan to improve the residential real estate industry by using technology to improve customer experience. We would like to see designs that use a black background. The final design should communicate sophistication and customer service, as well as stability and technology.

Industry/Entity Type

Real Estate

Requirements
Must have
• Black background

```html
<!DOCTYPE html>
<html lang="en">
<head>
<meta charset="utf-8">
<title>Velora Business Card</title>
<link href="https://fonts.googleapis.com/css2?family=Open+Sans:wght@400&display=swap" rel="stylesheet">
<style>
  :root {
    --backdrop: #5a5a5a;
    --card-top: #3a3536;
    --card-mid: #2a2627;
    --card-bottom: #1c1a1b;
    --brand-light: #e9eef4;
    --accent-blue: #3fa0de;
  }
  html, body {
    margin: 0;
    padding: 0;
    width: 1200px;
    height: 1023px;
    overflow: hidden;
    background: var(--backdrop);
  }
  .canvas {
    position: relative;
    width: 1200px;
    height: 1023px;
    display: flex;
    align-items: center;
    justify-content: center;
  }
  .business-card {
    position: relative;
    width: 500px;
    height: 875px;
    border-radius: 6px;
    background: linear-gradient(160deg, var(--card-top) 0%, var(--card-mid) 45%, var(--card-bottom) 100%);
    box-shadow: 0 20px 40px rgba(0,0,0,0.45);
    font-family: "Open Sans", sans-serif;
    overflow: hidden;
  }
  .brand-name {
    position: absolute;
    top: 120px;
    left: 0;
    right: 0;
    text-align: center;
    font-size: 58px;
    font-weight: 400;
    letter-spacing: 3px;
    color: var(--brand-light);
    margin: 0;
  }
  .contact-block {
    position: absolute;
    left: 48px;
    top: 520px;
    color: var(--accent-blue);
  }
  .contact-line {
    margin: 0;
    font-size: 24px;
    line-height: 34px;
    letter-spacing: 0.5px;
  }
  .person-name {
    margin: 14px 0 0;
    font-size: 36px;
    line-height: 44px;
  }
</style>
</head>
<body>
  <main class="canvas">
    <article class="business-card">
      <h1 class="brand-name">VELORA</h1>
      <div class="contact-block">
        <p class="contact-line">000. 000.0000</p>
        <p class="contact-line">info@velora.com</p>
        <p class="contact-line">www.velora.com</p>
        <p class="person-name">Dana Reyes</p>
      </div>
    </article>
  </main>
</body>
</html>
```